Create a web design for a vehicle codes lookup website

Create a bright and fun web design to replace our current boring one!

-Make a new design for this page that shows vehicle codes information: http://plinkor.net/vin/mara-dulek.4182.html
-Click "Random VIN" to see more examples.
-The page shows the vehicle information (see above example) is the most important one to add a redesign to. Bonus points if you create a redesign for the main page as well: plinkor.net.

Number of Pages Required

2 page

Requirements
Must have
• Be fun and have bright colors!
Should not have
• Do not add pictures of specific people or vehicles unless they can be used on every page. The example page has a Brevik Solano, but do not add a picture of the Brevik Solano because other pages have different vehicles.

```html
<!DOCTYPE html>
<html lang="en">
<head>
<meta charset="utf-8">
<title>Vehicle Purchase Information</title>
<link href="https://fonts.googleapis.com/css2?family=Open+Sans:wght@400;600;700;800&display=swap" rel="stylesheet">
<style>
:root{
  --blue:#1f56a8;
  --navy:#163f7e;
  --ink:#1d2a44;
  --bg:#eceff4;
  --label:#e3e9f2;
  --line:#d3dae6;
  --white:#ffffff;
  --muted:#6b7488;
  --footer:#1a3566;
}
*{box-sizing:border-box;margin:0;padding:0}
html,body{width:857px;height:1200px;overflow:hidden}
body{font-family:"Open Sans",Arial,sans-serif;background:var(--bg);color:var(--ink);position:relative}
.site-header{height:106px;background:var(--white);display:flex;align-items:center;padding:0 40px;justify-content:space-between}
.brand{display:flex;align-items:center;gap:14px}
.brand-mark{width:46px;height:46px;background:var(--blue);border-radius:8px;display:flex;align-items:center;justify-content:center}
.brand-vin{font-size:19px;font-weight:700;color:var(--navy);letter-spacing:.5px}
.brand-title{font-size:17px;font-weight:800;color:var(--ink)}
.search{display:flex;height:32px;width:236px;border:1px solid var(--line)}
.search span{flex:1;font-size:10px;color:var(--muted);padding:9px 10px}
.search b{width:32px;background:var(--blue);display:flex;align-items:center;justify-content:center}
.main-nav{height:26px;background:var(--navy);display:flex;justify-content:center}
.main-nav a{color:var(--white);font-size:9px;font-weight:600;text-decoration:none;padding:7px 26px;letter-spacing:.4px;border-right:1px solid rgba(255,255,255,.25)}
.main-nav a:last-child{border-right:0}
.banner{height:40px;margin:0 50px;background:var(--blue);display:flex;align-items:center;color:var(--white);position:relative}
.banner .icon{width:58px;height:40px;background:var(--white);display:flex;align-items:center;justify-content:center;border:1px solid var(--line)}
.banner h2{font-size:15px;font-weight:700;margin-left:40px;letter-spacing:.4px}
.customer{margin-top:40px}
.specs{margin:14px 50px 0;background:var(--white);display:grid;grid-template-columns:1fr 1fr;gap:0 18px;padding:18px 14px}
.specs table{width:100%;border-collapse:collapse;font-size:9.5px}
.specs td{height:36px;border-bottom:1px solid var(--line);padding:0 12px;font-weight:600}
.specs td.key{background:var(--label);color:var(--blue);width:40%;font-weight:700}
.fuel{margin-top:26px;height:50px}
.fuel h2{font-size:14px}
.fuel .icon{height:50px;width:70px}
.corner{position:absolute;right:10px;top:6px;font-size:16px;font-weight:700}
.bottom-nav{margin-top:34px}
.site-footer{background:var(--white);height:340px;margin-top:10px;padding:28px 30px;display:grid;grid-template-columns:1fr 1.2fr 1fr;gap:30px}
.site-footer h3{font-size:12px;font-weight:800;margin-bottom:14px}
.site-footer p{font-size:9px;color:var(--muted);line-height:1.6}
.news-field{display:flex;margin-top:12px;height:26px;border:1px solid var(--line);width:200px}
.news-field span{flex:1;font-size:8px;color:var(--muted);padding:7px 8px}
.news-field b{width:28px;background:var(--blue)}
.tweet{display:flex;gap:10px;margin-bottom:14px}
.dot{width:24px;height:24px;border-radius:50%;background:var(--blue);flex:none}
.tweet a{color:var(--blue)}
.contact-row{display:flex;gap:10px;margin-bottom:10px;align-items:flex-start}
.contact-row svg{flex:none;margin-top:2px}
.copyright{position:absolute;left:0;bottom:0;width:100%;height:34px;background:var(--footer);color:var(--white);font-size:8px;padding:12px 30px;letter-spacing:.4px}
</style>
</head>
<body>
<header class="site-header">
  <div class="brand">
    <div class="brand-mark"><svg width="28" height="20" viewBox="0 0 28 20"><path d="M4 11l3-7h14l3 7v6H4z" fill="none" stroke="#fff" stroke-width="2"/><circle cx="9" cy="15" r="2" fill="#fff"/><circle cx="19" cy="15" r="2" fill="#fff"/></svg></div>
    <div>
      <div class="brand-vin">0QKHP3EN3AW279436</div>
      <div class="brand-title">VEHICLE PURCHASE INFORMATION</div>
    </div>
  </div>
  <div class="search"><span>Get Vehicle Details...</span><b><svg width="12" height="12" viewBox="0 0 12 12"><circle cx="5" cy="5" r="3.5" fill="none" stroke="#fff" stroke-width="1.5"/><path d="M8 8l3 3" stroke="#fff" stroke-width="1.5"/></svg></b></div>
</header>
<nav class="main-nav">
  <a href="#">HOME</a><a href="#">SEARCH BY OWNER</a><a href="#">VIN LOOKUP</a><a href="#">COMPLETE LIST</a><a href="#">CONTACT US</a><a href="#">RANDOM VIN</a>
</nav>

<section class="banner customer">
  <div class="icon"><svg width="20" height="20" viewBox="0 0 20 20"><circle cx="10" cy="6" r="4" fill="#1f56a8"/><path d="M2 19c0-5 4-7 8-7s8 2 8 7z" fill="#1f56a8"/></svg></div>
  <h2>CUSTOMER NAME : MARA DULEK</h2>
</section>

<section class="specs">
  <table>
    <tr><td class="key">ADDRESS</td><td>4120 ORMOND AVE E</td></tr>
    <tr><td class="key">CITY</td><td>FALKTON</td></tr>
    <tr><td class="key">STATE</td><td>WA</td></tr>
    <tr><td class="key">ZIP</td><td>98412-3307</td></tr>
    <tr><td class="key">YEAR</td><td>2007</td></tr>
    <tr><td class="key">MAKE</td><td>BREVIK</td></tr>
    <tr><td class="key">MODEL</td><td>SOLANO</td></tr>
    <tr><td class="key">VIN</td><td>0ZRKS40R271054829</td></tr>
    <tr><td class="key">TRIM LEVEL</td><td>CONVERTIBLE LT3</td></tr>
    <tr><td class="key">ENGINE</td><td>6.0L V8 OHV 16V</td></tr>
    <tr><td class="key">STYLE</td><td>CONVERTIBLE 2-DR</td></tr>
    <tr><td class="key">MADE IN</td><td>UNITED STATES</td></tr>
  </table>
  <table>
    <tr><td class="key">STEERING TYPE</td><td>R&amp;P</td></tr>
    <tr><td class="key">ANTI-BRAKE SYSTEM</td><td>4-WHEEL ABS</td></tr>
    <tr><td class="key">TANK SIZE</td><td>18.00 GALLON</td></tr>
    <tr><td class="key">OVERALL HEIGHT</td><td>49.10 IN.</td></tr>
    <tr><td class="key">OVERALL LENGTH</td><td>174.60 IN.</td></tr>
    <tr><td class="key">OVERALL WIDTH</td><td>72.60 IN.</td></tr>
    <tr><td class="key">STANDARD SEATING</td><td>2</td></tr>
    <tr><td class="key">OPTIONAL SEATING</td><td>NO DATA</td></tr>
    <tr><td class="key">HIGHWAY MILEAGE</td><td>27 - 28 MILES/GALLON</td></tr>
    <tr><td class="key">CITY MILEAGE</td><td>17 - 18 MILES/GALLON</td></tr>
    <tr><td class="key">TRANSMISSION</td><td>6-SPEED AUTOMATIC</td></tr>
    <tr><td class="key">&nbsp;</td><td></td></tr>
  </table>
</section>

<section class="banner fuel">
  <div class="icon"><svg width="22" height="26" viewBox="0 0 22 26"><rect x="2" y="4" width="13" height="20" rx="2" fill="#1f56a8"/><rect x="5" y="7" width="7" height="5" fill="#fff"/><path d="M15 10h3v10a2 2 0 0 0 3 0V8l-3-4" fill="none" stroke="#1f56a8" stroke-width="2"/></svg></div>
  <h2>NATIONAL FUEL BUREAU ECONOMY INFORMATION</h2>
  <span class="corner">+</span>
</section>

<nav class="main-nav bottom-nav">
  <a href="#">HOME</a><a href="#">SEARCH BY OWNER</a><a href="#">VIN LOOKUP</a><a href="#">COMPLETE LIST</a><a href="#">CONTACT US</a><a href="#">RANDOM VIN</a>
</nav>

<footer class="site-footer">
  <div>
    <h3>SIGNUP FOR NEWSLETTER</h3>
    <p>Select your newsletters, enter your email address, and click "subscribe"</p>
    <div class="news-field"><span>Enter your email address</span><b></b></div>
  </div>
  <div>
    <h3>RECENT TWEETS</h3>
    <div class="tweet"><span class="dot"></span><p><a>@plinkor.net</a> Hi There You Can Contact Page Form on http://www.plinkor.net/contact</p></div>
    <div class="tweet"><span class="dot"></span><p><a>@plinkor.net</a> Hi There You Can Use Contact Page Form on http://www.plinkor.net/contact</p></div>
  </div>
  <div>
    <h3>CONTACT US</h3>
    <div class="contact-row"><svg width="10" height="12" viewBox="0 0 10 12"><path d="M5 0a4 4 0 0 1 4 4c0 3-4 8-4 8S1 7 1 4a4 4 0 0 1 4-4z" fill="#1f56a8"/></svg><p>Sample Street, 14 Harrow Lane, Eastfield Road, United Kingdom</p></div>
    <div class="contact-row"><svg width="10" height="10" viewBox="0 0 10 10"><path d="M1 1h3l1 2-1.5 1a6 6 0 0 0 2.5 2.5L7 5l2 1v3c-5 0-8-3-8-8z" fill="#1f56a8"/></svg><p>1 555 014 2290</p></div>
    <div class="contact-row"><svg width="11" height="8" viewBox="0 0 11 8"><rect width="11" height="8" fill="#1f56a8"/><path d="M0 0l5.5 4L11 0" stroke="#fff" fill="none"/></svg><p>info@plinkor.net</p></div>
  </div>
</footer>
<div class="copyright">© COPYRIGHT 2016 PLINKOR.NET</div>
</body>
</html>
```